Digital Transformation Company Template Slidedeck

I am looking for help designing a set of standard business powerpoint slides that are branded specifically for my company. I have attached more details and the logo design file that can be used for this project. Thanks!

Target Market(s)

Small and Medium Businesses

```html
<!DOCTYPE html>
<html lang="en">
<head>
<meta charset="utf-8">
<title>Veltrion Tech – Slide Deck Template</title>
<link rel="stylesheet" href="https://fonts.googleapis.com/css2?family=Ubuntu:wght@300;400;500;700&display=swap">
<style>
:root{
  --orange:#e8661c;
  --blue:#2f8fe0;
  --navy:#1d3557;
  --ink:#2b2d31;
  --dark:#232427;
  --grey:#6b6e75;
  --page:#d9dadd;
  --white:#ffffff;
}
*{box-sizing:border-box;margin:0;padding:0}
html,body{width:1200px;height:2424px;overflow:hidden}
body{position:relative;background:var(--page);font-family:'Ubuntu',sans-serif;color:var(--ink)}
h1,h2{font-weight:400}
.hero{position:absolute;left:0;top:0;width:1200px;height:716px;background:linear-gradient(180deg,#c9cfdb 0%,#dfe2e8 60%,#d9dadd 100%)}
.hero-brand{position:absolute;right:52px;top:52px;font-size:30px;font-weight:700;color:var(--orange);letter-spacing:1px}
.hero-slide{position:absolute;left:122px;top:130px;transform:scale(1.7);transform-origin:0 0;box-shadow:0 6px 18px rgba(0,0,0,.25)}

.slide{position:absolute;width:562px;height:316px;background:var(--white);overflow:hidden}
.col-a{left:28px}.col-b{left:610px}
.row-1{top:734px}.row-2{top:1069px}.row-3{top:1404px}.row-4{top:1739px}.row-5{top:2074px}
.abs{position:absolute}

.brand{position:absolute;font-weight:700;color:var(--ink);white-space:nowrap;display:flex;align-items:center;gap:4px}
.brand .mark{display:inline-block;background:var(--orange)}
.footer .brand{left:15px;top:283px;font-size:10px}
.footer .brand .mark{width:7px;height:7px}
.footer .copy{position:absolute;right:35px;top:288px;font-size:5.5px;color:var(--grey)}
.footer .page{position:absolute;right:15px;top:285px;width:11px;height:11px;border:1px solid var(--orange);border-radius:50%;font-size:5.5px;color:var(--orange);text-align:center;line-height:9px}

.photo{position:absolute}
.kicker{position:absolute;left:35px;top:34px;font-size:9px;color:var(--blue)}
.h-side{position:absolute;left:35px;font-size:19px;font-weight:400;color:var(--navy);line-height:21px}
.h-center{position:absolute;left:0;width:100%;text-align:center;font-size:18px;font-weight:400;color:var(--navy)}
.body{font-size:7px;line-height:8.4px;color:var(--grey)}

/* title slide */
.t-brand{left:49px;top:50px;font-size:15px}
.t-brand .mark{width:10px;height:10px}
.t-title{left:49px;top:108px;font-size:27px;font-weight:700;line-height:29.5px;color:var(--ink)}
.t-rule{left:49px;top:172px;width:208px;height:2px;background:linear-gradient(90deg,var(--orange),var(--blue))}
.t-sub{left:49px;top:181px;font-size:11px;color:var(--ink)}
.t-date{left:49px;top:206px;font-size:6.5px;color:var(--ink)}
.t-btn{left:49px;top:232px;width:91px;height:15px;background:var(--blue);border-radius:2px;color:var(--white);font-size:6px;text-align:center;line-height:15px}
.t-bar{left:0;top:296px;width:100%;height:20px;background:var(--dark);color:#cfd0d3;font-size:5.5px;text-align:center;line-height:20px}

/* toc */
.toc-item{position:absolute;width:200px}
.toc-num{position:absolute;left:0;top:0;font-size:19px;color:var(--orange)}
.toc-title{position:absolute;left:27px;top:-1px;font-size:11px;color:var(--ink)}
.toc-desc{position:absolute;left:27px;top:13px;width:170px;font-size:6px;line-height:7px;color:var(--grey)}

/* about */
.card{position:absolute;top:158px;height:59px;border:1px solid #e3e4e7;border-radius:4px;background:var(--white)}
.card-icon{position:absolute;left:-14px;top:15px;width:28px;height:28px;border-radius:50%;background:var(--orange)}
.card-title{position:absolute;left:20px;top:8px;font-size:9.5px;color:var(--blue)}
.card-text{position:absolute;left:20px;top:22px;width:78px;font-size:5.5px;line-height:6.3px;color:var(--grey)}

/* icon circles */
.ico{position:absolute;border-radius:50%;display:flex;align-items:center;justify-content:center}
.ico.dark{background:var(--dark)}.ico.orange{background:var(--orange)}.ico.blue{background:var(--blue)}
.col-head{position:absolute;text-align:center;font-size:10px}
.col-text{position:absolute;text-align:center;font-size:6.8px;line-height:8px;color:var(--grey)}

.stat{position:absolute;width:80px;text-align:center}
.stat .num{font-size:25px;margin-top:4px}
.stat .lab{font-size:9.5px;margin-top:8px}
.stat .txt{font-size:6.5px;line-height:7.6px;color:var(--grey);margin:8px auto 0;width:58px}

.feat-head{position:absolute;font-size:9px}
.feat-text{position:absolute;width:100px;font-size:5.8px;line-height:6.6px;color:var(--grey)}

.bullets{position:absolute;left:35px;top:104px;width:222px;list-style:none}
.bullets li{position:relative;padding-left:12px;margin-bottom:7px;font-size:7px;line-height:8.2px;color:var(--grey)}
.bullets li::before{content:"";position:absolute;left:0;top:3px;width:3px;height:3px;background:var(--orange);border-radius:50%}

/* closing */
.closing{background:var(--dark)}
.c-brand{left:50px;top:122px;font-size:16px;color:var(--white)}
.c-brand .mark{width:10px;height:10px}
.c-head{left:50px;top:170px;font-size:11px;font-weight:500;color:var(--white)}
.c-line{position:absolute;left:50px;font-size:7px;color:var(--white);display:flex;align-items:center;gap:8px}
.c-bar{left:0;top:298px;width:100%;height:18px;background:#eceef0;font-size:5.5px;color:var(--grey);text-align:center;line-height:18px}
</style>
</head>
<body>

<section class="hero">
  <div class="hero-brand">Veltrion Tech</div>
</section>

<!-- Title slide (large preview) -->
<article class="slide hero-slide">
  <svg class="abs" width="562" height="316" viewBox="0 0 562 316">
    <defs><linearGradient id="pg1" x1="0" y1="0" x2="1" y2="1"><stop offset="0" stop-color="#7a5a44"/><stop offset="1" stop-color="#c99a72"/></linearGradient></defs>
    <polygon points="461,0 562,0 562,296 268,296" fill="url(#pg1)" role="img" aria-label="Photo of two colleagues smiling at a laptop"/>
    <polygon points="461,0 530,0 337,296 268,296" fill="#2f8fe0" opacity=".88"/>
    <polygon points="390,0 432,0 343,136 301,136" fill="#e8661c"/>
  </svg>
  <div class="brand abs t-brand"><span class="mark"></span>Veltrion Tech</div>
  <h1 class="abs t-title">Presentation<br>Title Goes Here</h1>
  <div class="abs t-rule"></div>
  <div class="abs t-sub">Subtitle of Presentation Goes Here</div>
  <div class="abs t-date">Wednesday, January 25, 2023</div>
  <div class="abs t-btn">www.veltrion.io</div>
  <div class="abs t-bar">Copyright © 2021 Veltrion Technology, LLC. All Rights Reserved.</div>
</article>

<!-- 1 Title -->
<article class="slide col-a row-1">
  <svg class="abs" width="562" height="316" viewBox="0 0 562 316">
    <defs><linearGradient id="pg2" x1="0" y1="0" x2="1" y2="1"><stop offset="0" stop-color="#7a5a44"/><stop offset="1" stop-color="#c99a72"/></linearGradient></defs>
    <polygon points="461,0 562,0 562,296 268,296" fill="url(#pg2)" role="img" aria-label="Photo of two colleagues smiling at a laptop"/>
    <polygon points="461,0 530,0 337,296 268,296" fill="#2f8fe0" opacity=".88"/>
    <polygon points="390,0 432,0 343,136 301,136" fill="#e8661c"/>
  </svg>
  <div class="brand abs t-brand"><span class="mark"></span>Veltrion Tech</div>
  <h1 class="abs t-title">Presentation<br>Title Goes Here</h1>
  <div class="abs t-rule"></div>
  <div class="abs t-sub">Subtitle of Presentation Goes Here</div>
  <div class="abs t-date">Wednesday, January 25, 2023</div>
  <div class="abs t-btn">www.veltrion.io</div>
  <div class="abs t-bar">Copyright © 2021 Veltrion Technology, LLC. All Rights Reserved.</div>
</article>

<!-- 2 Table of contents -->
<article class="slide col-b row-1">
  <h2 class="h-center" style="top:24px">Table of Contents</h2>
  <div class="toc-item" style="left:76px;top:98px"><span class="toc-num">1</span><span class="toc-title">Title Goes Here</span><p class="toc-desc">Vivamus eu dui ex. Curabitur dapibus dignissim dui, in molestie metus feugiat sed.</p></div>
  <div class="toc-item" style="left:298px;top:98px"><span class="toc-num">2</span><span class="toc-title">Title Goes Here</span><p class="toc-desc">Vivamus eu dui ex. Curabitur dapibus dignissim dui, in molestie metus feugiat sed.</p></div>
  <div class="toc-item" style="left:76px;top:153px"><span class="toc-num">3</span><span class="toc-title">Title Goes Here</span><p class="toc-desc">Vivamus eu dui ex. Curabitur dapibus dignissim dui, in molestie metus feugiat sed.</p></div>
  <div class="toc-item" style="left:298px;top:153px"><span class="toc-num">4</span><span class="toc-title">Title Goes Here</span><p class="toc-desc">Vivamus eu dui ex. Curabitur dapibus dignissim dui, in molestie metus feugiat sed.</p></div>
  <div class="toc-item" style="left:76px;top:208px"><span class="toc-num">5</span><span class="toc-title">Title Goes Here</span><p class="toc-desc">Vivamus eu dui ex. Curabitur dapibus dignissim dui, in molestie metus feugiat sed.</p></div>
  <div class="toc-item" style="left:298px;top:208px"><span class="toc-num">6</span><span class="toc-title">Title Goes Here</span><p class="toc-desc">Vivamus eu dui ex. Curabitur dapibus dignissim dui, in molestie metus feugiat sed.</p></div>
  <div class="footer"><div class="brand"><span class="mark"></span>Veltrion Tech</div><div class="copy">Copyright © 2021 Veltrion Technology, LLC. All Rights Reserved.</div><div class="page">2</div></div>
</article>

<!-- 3 About -->
<article class="slide col-a row-2">
  <div class="kicker">ABOUT US</div>
  <h2 class="h-side" style="top:50px">We are the nexus of operating<br>in the digital age</h2>
  <p class="abs body" style="left:35px;top:113px;width:270px">Our team includes veterans from the world's premier military, technology and cybersecurity organizations. Our experienced personnel of technical experts provide solutions to the toughest challenges in the digital arena.</p>
  <div class="card" style="left:52px;width:108px"><span class="card-icon"></span><span class="card-title">Experience</span><p class="card-text">Our great team has 20+ years delivering secure technical solutions.</p></div>
  <div class="card" style="left:190px;width:116px"><span class="card-icon"></span><span class="card-title">Quick Support</span><p class="card-text">We will gladly join your team on their journey of adapting and testing bold new ideas.</p></div>
  <p class="abs body" style="left:35px;top:234px;width:270px;font-size:6px;line-height:7px">No matter if you are just getting started or have been in business for years, we can help you leverage technology to your advantage.</p>
  <svg class="abs" style="left:320px;top:40px" width="240" height="220" viewBox="0 0 240 220">
    <polygon points="70,45 105,10 140,45 105,80" fill="#eef1f5"/>
    <polygon points="25,95 60,60 95,95 60,130" fill="#eef1f5"/>
    <polygon points="150,95 185,60 220,95 185,130" fill="#eef1f5"/>
    <polygon points="125,5 190,70 125,135 60,70" fill="#b9a792" role="img" aria-label="Portrait photo of a smiling team member"/>
    <polygon points="70,115 105,80 140,115 105,150" fill="#c9ccd2" role="img" aria-label="Photo of a team meeting"/>
    <polygon points="150,125 180,95 210,125 180,155" fill="#d7dade"/>
    <polygon points="130,160 160,190 130,220 100,190" fill="#1b1c1f"/>
    <polygon points="30,140 150,140 150,175 30,175" fill="#1d3557"/>
    <polygon points="150,145 165,160 150,175 160,175 175,160 160,145" fill="#e8661c"/>
    <polygon points="165,145 180,160 165,175 175,175 190,160 175,145" fill="#2f8fe0"/>
    <text x="44" y="156" font-family="Ubuntu,sans-serif" font-size="9" fill="#fff">20+ years</text>
    <text x="50" y="168" font-family="Ubuntu,sans-serif" font-size="4.5" fill="#fff">Technical Experience</text>
  </svg>
  <div class="footer"><div class="brand"><span class="mark"></span>Veltrion Tech</div><div class="copy">Copyright © 2021 Veltrion Technology, LLC. All Rights Reserved.</div><div class="page">3</div></div>
</article>

<!-- 4 Mission -->
<article class="slide col-b row-2">
  <div class="photo" style="left:15px;top:16px;width:532px;height:141px;background:linear-gradient(180deg,#6b5a4a 0%,#d99a4e 55%,#2a2420 100%)" role="img" aria-label="Photo of a group jumping on a beach at sunset"></div>
  <h2 class="h-center" style="top:178px">Our Mission</h2>
  <p class="abs body" style="left:19px;top:207px;width:524px;text-align:justify;font-size:6.9px;line-height:8px">Veltrion is a digital transformation consulting firm that provides tailored software solutions, cybersecurity assessments and business operations consulting to ensure that our clients can thrive in the digital age. By helping businesses securely design, implement, and optimize their digital initiatives, we are able to help them minimize costs, reduce risk, and deliver better experiences for their customers. Our mandate is to strive to be the nexus of operating in the digital age while helping our clients achieve their next goal. No matter if you are just getting started or have been in business for years, we can help you leverage technology to your advantage.</p>
  <div class="footer"><div class="brand"><span class="mark"></span>Veltrion Tech</div><div class="copy">Copyright © 2021 Veltrion Technology, LLC. All Rights Reserved.</div><div class="page">4</div></div>
</article>

<!-- 5 Services -->
<article class="slide col-a row-3">
  <div class="kicker">OUR SERVICE</div>
  <h2 class="h-side" style="top:50px">We Offer a Wide Variety of<br>Digital Services</h2>
  <p class="abs body" style="left:316px;top:52px;width:218px">There is a global shift occurring through digitalization and technology. Competition is getting fierce and cyber threats to businesses are growing each day. Let us help you navigate the digital terrain.</p>
  <div class="photo" style="left:30px;top:113px;width:163px;height:74px;background:linear-gradient(135deg,#8a8f98,#3f4652)" role="img" aria-label="Photo of people working with a laptop"></div>
  <div class="photo" style="left:199px;top:113px;width:163px;height:74px;background:linear-gradient(135deg,#2a3a30,#101312)" role="img" aria-label="Photo of code on a screen"></div>
  <div class="photo" style="left:368px;top:113px;width:163px;height:74px;background:linear-gradient(135deg,#e5e8ec,#6a7a8c)" role="img" aria-label="Photo of a laptop on a desk"></div>
  <div class="col-head" style="left:30px;top:198px;width:163px;color:var(--orange)">Heading Goes Here</div>
  <div class="col-head" style="left:199px;top:198px;width:163px;color:var(--orange)">Heading Goes Here</div>
  <div class="col-head" style="left:368px;top:198px;width:163px;color:var(--orange)">Heading Goes Here</div>
  <p class="col-text" style="left:35px;top:215px;width:153px">Lorem ipsum dolor sit amet, consectetur adipiscing elit. Vivamus eu dui ex. Curabitur dapibus dignissim dui, in molestie metus feugiat sed. Praesent aliquet lorem ex.</p>
  <p class="col-text" style="left:204px;top:215px;width:153px">Lorem ipsum dolor sit amet, consectetur adipiscing elit. Vivamus eu dui ex. Curabitur dapibus dignissim dui, in molestie metus feugiat sed. Praesent aliquet lorem ex.</p>
  <p class="col-text" style="left:373px;top:215px;width:153px">Lorem ipsum dolor sit amet, consectetur adipiscing elit. Vivamus eu dui ex. Curabitur dapibus dignissim dui, in molestie metus feugiat sed. Praesent aliquet lorem ex.</p>
  <div class="footer"><div class="brand"><span class="mark"></span>Veltrion Tech</div><div class="copy">Copyright © 2021 Veltrion Technology, LLC. All Rights Reserved.</div><div class="page">5</div></div>
</article>

<!-- 6 Three columns -->
<article class="slide col-b row-3">
  <h2 class="h-center" style="top:22px">Heading Goes Here</h2>
  <p class="abs body" style="left:45px;top:58px;width:472px;text-align:center">Lorem ipsum dolor sit amet, consectetur adipiscing elit. Vivamus eu dui ex. Curabitur dapibus dignissim dui, in molestie metus feugiat sed. Praesent aliquet lorem ex, eu dapibus odio varius at. Duis eget tellus porta, consequat lacus vitae, venenatis dolor. Nulla facilisi. In et sollicitudin lacus. Donec risus orci, gravida sit amet risus vehicula, aliquet pretium sapien.</p>
  <div class="ico dark" style="left:90px;top:109px;width:50px;height:50px"><svg width="24" height="20" viewBox="0 0 24 20"><rect x="9" y="0" width="6" height="5" fill="#fff"/><rect x="0" y="14" width="6" height="5" fill="#fff"/><rect x="9" y="14" width="6" height="5" fill="#fff"/><rect x="18" y="14" width="6" height="5" fill="#fff"/><path d="M12 5v5M3 14v-4h18v4M12 10v4" stroke="#fff" stroke-width="1.5" fill="none"/></svg></div>
  <div class="ico orange" style="left:255px;top:109px;width:50px;height:50px"><svg width="26" height="16" viewBox="0 0 26 16"><path d="M6 16a6 6 0 0 1 0-12 8 8 0 0 1 15 3 4.5 4.5 0 0 1 0 9z" fill="#fff"/></svg></div>
  <div class="ico blue" style="left:420px;top:109px;width:50px;height:50px"><svg width="26" height="20" viewBox="0 0 26 20"><rect x="3" y="1" width="20" height="13" rx="1" fill="none" stroke="#fff" stroke-width="2"/><rect x="0" y="16" width="26" height="3" fill="#fff"/></svg></div>
  <div class="col-head" style="left:45px;top:171px;width:140px;color:var(--ink)">Heading Goes Here</div>
  <div class="col-head" style="left:210px;top:171px;width:140px;color:var(--ink)">Heading Goes Here</div>
  <div class="col-head" style="left:375px;top:171px;width:140px;color:var(--ink)">Heading Goes Here</div>
  <p class="col-text" style="left:45px;top:189px;width:140px">Lorem ipsum dolor sit amet, consectetur adipiscing elit. Vivamus eu dui ex. Curabitur dapibus dignissim dui, in molestie metus feugiat sed. Praesent aliquet lorem ex.</p>
  <p class="col-text" style="left:210px;top:189px;width:140px">Lorem ipsum dolor sit amet, consectetur adipiscing elit. Vivamus eu dui ex. Curabitur dapibus dignissim dui, in molestie metus feugiat sed. Praesent aliquet lorem ex.</p>
  <p class="col-text" style="left:375px;top:189px;width:140px">Lorem ipsum dolor sit amet, consectetur adipiscing elit. Vivamus eu dui ex. Curabitur dapibus dignissim dui, in molestie metus feugiat sed. Praesent aliquet lorem ex.</p>
  <div class="footer"><div class="brand"><span class="mark"></span>Veltrion Tech</div><div class="copy">Copyright © 2021 Veltrion Technology, LLC. All Rights Reserved.</div><div class="page">6</div></div>
</article>

<!-- 7 Stats -->
<article class="slide col-a row-4">
  <h2 class="h-side" style="top:54px">Pellentesque habitant<br>morbi tristique senectus</h2>
  <ul class="bullets">
    <li>Lorem ipsum dolor sit amet, consectetur adipiscing elit. Vivamus eu dui ex. Curabitur dapibus dignissim dui, in molestie metus feugiat sed.</li>
    <li>Praesent aliquet lorem ex, eu dapibus odio varius at. Duis eget tellus porta, consequat lacus vitae, venenatis dolor. Nulla facilisi. In et sollicitudin lacus.</li>
    <li>Donec risus orci, gravida sit amet risus vehicula, aliquet pretium sapien.</li>
    <li>Nullam sit amet magna non ex bibendum mollis. Nunc vel neque eu augue dignissim congue ut vitae magna.</li>
  </ul>
  <div class="stat" style="left:277px;top:66px"><div class="ico dark" style="position:relative;margin:0 auto;width:40px;height:40px"><svg width="20" height="20" viewBox="0 0 20 20"><circle cx="10" cy="10" r="8" fill="none" stroke="#fff" stroke-width="1.8"/><path d="M10 5v5h4" stroke="#fff" stroke-width="1.8" fill="none"/></svg></div><div class="num" style="color:var(--ink)">45%</div><div class="lab">Heading</div><p class="txt">Lorem ipsum dolor sit amet, consectetur adipiscing elit. Vivamus eu dui ex. Curabitur dapibus dignissim dui.</p></div>
  <div class="stat" style="left:365px;top:66px"><div class="ico orange" style="position:relative;margin:0 auto;width:40px;height:40px"><svg width="16" height="19" viewBox="0 0 16 19"><path d="M8 1l7 3v5c0 5-3.5 8-7 9-3.5-1-7-4-7-9V4z" fill="none" stroke="#fff" stroke-width="1.8"/></svg></div><div class="num" style="color:var(--orange)">82%</div><div class="lab" style="color:var(--orange)">Heading</div><p class="txt">Lorem ipsum dolor sit amet, consectetur adipiscing elit. Vivamus eu dui ex. Curabitur dapibus dignissim dui.</p></div>
  <div class="stat" style="left:453px;top:66px"><div class="ico blue" style="position:relative;margin:0 auto;width:40px;height:40px"><svg width="22" height="17" viewBox="0 0 22 17"><rect x="2" y="1" width="18" height="11" rx="1" fill="none" stroke="#fff" stroke-width="1.8"/><rect x="0" y="14" width="22" height="2.5" fill="#fff"/></svg></div><div class="num" style="color:var(--blue)">76%</div><div class="lab" style="color:var(--blue)">Heading</div><p class="txt">Lorem ipsum dolor sit amet, consectetur adipiscing elit. Vivamus eu dui ex. Curabitur dapibus dignissim dui.</p></div>
  <div class="footer"><div class="brand"><span class="mark"></span>Veltrion Tech</div><div class="copy">Copyright © 2021 Veltrion Technology, LLC. All Rights Reserved.</div><div class="page">7</div></div>
</article>

<!-- 8 Features with photo -->
<article class="slide col-b row-4">
  <div class="photo" style="left:36px;top:0;width:153px;height:267px;background:linear-gradient(180deg,#3e5a3a 0%,#2a3440 55%,#8d9aa8 100%)" role="img" aria-label="Photo of a man working on a laptop in front of code"></div>
  <h2 class="abs" style="left:217px;top:42px;font-size:18px;font-weight:400;color:var(--navy)">Heading Goes Here</h2>
  <p class="abs body" style="left:217px;top:78px;width:310px">Lorem ipsum dolor sit amet, consectetur adipiscing elit. Vivamus eu dui ex. Curabitur dapibus dignissim dui, in molestie metus feugiat sed. Praesent aliquet lorem ex, eu dapibus odio varius at. Duis eget tellus porta, consequat lacus vitae.</p>
  <div class="ico orange" style="left:212px;top:147px;width:34px;height:34px"><svg width="12" height="17" viewBox="0 0 12 17"><path d="M6 1a5 5 0 0 0-3 9v3h6v-3a5 5 0 0 0-3-9z" fill="none" stroke="#fff" stroke-width="1.6"/><rect x="3" y="14" width="6" height="2" fill="#fff"/></svg></div>
  <div class="ico blue" style="left:376px;top:147px;width:34px;height:34px"><svg width="18" height="18" viewBox="0 0 18 18"><circle cx="9" cy="9" r="6" fill="none" stroke="#fff" stroke-width="2.5" stroke-dasharray="3 1.7"/><circle cx="9" cy="9" r="2.5" fill="#fff"/></svg></div>
  <div class="ico blue" style="left:212px;top:209px;width:34px;height:34px"><svg width="18" height="14" viewBox="0 0 18 14"><rect x="2" y="1" width="14" height="9" rx="1" fill="none" stroke="#fff" stroke-width="1.6"/><rect x="0" y="11" width="18" height="2" fill="#fff"/></svg></div>
  <div class="ico orange" style="left:376px;top:209px;width:34px;height:34px"><svg width="14" height="16" viewBox="0 0 14 16"><path d="M7 1l6 2.5v4c0 4-3 7-6 8-3-1-6-4-6-8v-4z" fill="none" stroke="#fff" stroke-width="1.6"/></svg></div>
  <div class="feat-head" style="left:262px;top:144px;color:var(--orange)">Heading Goes Here</div>
  <div class="feat-head" style="left:425px;top:144px;color:var(--blue)">Heading Goes Here</div>
  <div class="feat-head" style="left:262px;top:207px;color:var(--blue)">Heading Goes Here</div>
  <div class="feat-head" style="left:425px;top:207px;color:var(--orange)">Heading Goes Here</div>
  <p class="feat-text" style="left:262px;top:157px">Lorem ipsum dolor sit amet, consectetur adipiscing elit. Vivamus eu dui ex. Curabitur dapibus dignissim dui, in molestie metus feugiat sed.</p>
  <p class="feat-text" style="left:425px;top:157px">Lorem ipsum dolor sit amet, consectetur adipiscing elit. Vivamus eu dui ex. Curabitur dapibus dignissim dui, in molestie metus feugiat sed.</p>
  <p class="feat-text" style="left:262px;top:220px">Lorem ipsum dolor sit amet, consectetur adipiscing elit. Vivamus eu dui ex. Curabitur dapibus dignissim dui, in molestie metus feugiat sed.</p>
  <p class="feat-text" style="left:425px;top:220px">Lorem ipsum dolor sit amet, consectetur adipiscing elit. Vivamus eu dui ex. Curabitur dapibus dignissim dui, in molestie metus feugiat sed.</p>
  <div class="footer"><div class="brand"><span class="mark"></span>Veltrion Tech</div><div class="copy">Copyright © 2021 Veltrion Technology, LLC. All Rights Reserved.</div><div class="page">8</div></div>
</article>

<!-- 9 Chart -->
<article class="slide col-a row-5">
  <h2 class="h-center" style="top:22px">Heading Goes Here</h2>
  <svg class="abs" style="left:0;top:0" width="562" height="316" viewBox="0 0 562 316" font-family="Ubuntu,sans-serif" font-size="6" fill="#6b6e75">
    <g stroke="#e3e4e7" stroke-width=".6">
      <line x1="73" y1="87" x2="512" y2="87"/><line x1="73" y1="102" x2="512" y2="102"/><line x1="73" y1="117" x2="512" y2="117"/><line x1="73" y1="132" x2="512" y2="132"/><line x1="73" y1="147" x2="512" y2="147"/><line x1="73" y1="162" x2="512" y2="162"/><line x1="73" y1="176" x2="512" y2="176"/><line x1="73" y1="191" x2="512" y2="191"/><line x1="73" y1="206" x2="512" y2="206"/><line x1="73" y1="221" x2="512" y2="221"/><line x1="73" y1="236" x2="512" y2="236" stroke="#bfc1c5"/>
    </g>
    <g text-anchor="end">
      <text x="68" y="89">10,000</text><text x="68" y="104">9,000</text><text x="68" y="119">8,000</text><text x="68" y="134">7,000</text><text x="68" y="149">6,000</text><text x="68" y="164">5,000</text><text x="68" y="178">4,000</text><text x="68" y="193">3,000</text><text x="68" y="208">2,000</text><text x="68" y="223">1,000</text><text x="68" y="238">0</text>
    </g>
    <g>
      <rect x="81" y="221" width="5" height="15" fill="#232427"/><rect x="87" y="206" width="5" height="30" fill="#e8661c"/><rect x="93" y="176" width="5" height="60" fill="#2f8fe0"/>
      <rect x="112" y="191" width="5" height="45" fill="#232427"/><rect x="118" y="221" width="5" height="15" fill="#e8661c"/><rect x="124" y="206" width="5" height="30" fill="#2f8fe0"/>
      <rect x="144" y="162" width="5" height="74" fill="#232427"/><rect x="150" y="221" width="5" height="15" fill="#e8661c"/><rect x="156" y="191" width="5" height="45" fill="#2f8fe0"/>
      <rect x="175" y="221" width="5" height="15" fill="#232427"/><rect x="181" y="176" width="5" height="60" fill="#e8661c"/><rect x="187" y="117" width="5" height="119" fill="#2f8fe0"/>
      <rect x="207" y="117" width="5" height="119" fill="#232427"/><rect x="213" y="176" width="5" height="60" fill="#e8661c"/><rect x="219" y="162" width="5" height="74" fill="#2f8fe0"/>
      <rect x="238" y="132" width="5" height="104" fill="#232427"/><rect x="244" y="191" width="5" height="45" fill="#e8661c"/><rect x="250" y="206" width="5" height="30" fill="#2f8fe0"/>
      <rect x="269" y="191" width="5" height="45" fill="#232427"/><rect x="275" y="221" width="5" height="15" fill="#e8661c"/><rect x="281" y="176" width="5" height="60" fill="#2f8fe0"/>
      <rect x="301" y="162" width="5" height="74" fill="#232427"/><rect x="307" y="206" width="5" height="30" fill="#e8661c"/><rect x="313" y="102" width="5" height="134" fill="#2f8fe0"/>
      <rect x="332" y="191" width="5" height="45" fill="#232427"/><rect x="338" y="132" width="5" height="104" fill="#e8661c"/><rect x="344" y="176" width="5" height="60" fill="#2f8fe0"/>
      <rect x="364" y="191" width="5" height="45" fill="#232427"/><rect x="370" y="102" width="5" height="134" fill="#e8661c"/><rect x="376" y="191" width="5" height="45" fill="#2f8fe0"/>
      <rect x="395" y="162" width="5" height="74" fill="#232427"/><rect x="401" y="221" width="5" height="15" fill="#e8661c"/><rect x="407" y="206" width="5" height="30" fill="#2f8fe0"/>
      <rect x="426" y="221" width="5" height="15" fill="#232427"/><rect x="432" y="176" width="5" height="60" fill="#e8661c"/><rect x="438" y="162" width="5" height="74" fill="#2f8fe0"/>
      <rect x="458" y="176" width="5" height="60" fill="#232427"/><rect x="464" y="206" width="5" height="30" fill="#e8661c"/><rect x="470" y="117" width="5" height="119" fill="#2f8fe0"/>
      <rect x="489" y="191" width="5" height="45" fill="#232427"/><rect x="495" y="147" width="5" height="89" fill="#e8661c"/><rect x="501" y="206" width="5" height="30" fill="#2f8fe0"/>
    </g>
    <g text-anchor="middle">
      <text x="89" y="246">2011</text><text x="120" y="246">2012</text><text x="152" y="246">2013</text><text x="183" y="246">2014</text><text x="215" y="246">2015</text><text x="246" y="246">2016</text><text x="277" y="246">2017</text><text x="309" y="246">2018</text><text x="340" y="246">2019</text><text x="372" y="246">2020</text><text x="403" y="246">2021</text><text x="434" y="246">2022</text><text x="466" y="246">2023</text><text x="497" y="246">2024</text>
    </g>
  </svg>
  <div class="footer"><div class="brand"><span class="mark"></span>Veltrion Tech</div><div class="copy">Copyright © 2021 Veltrion Technology, LLC. All Rights Reserved.</div><div class="page">9</div></div>
</article>

<!-- 10 Closing -->
<article class="slide col-b row-5 closing">
  <svg class="abs" width="562" height="316" viewBox="0 0 562 316">
    <defs><linearGradient id="pg3" x1="0" y1="0" x2="1" y2="1"><stop offset="0" stop-color="#7a5a44"/><stop offset="1" stop-color="#c99a72"/></linearGradient></defs>
    <polygon points="470,0 562,0 562,298 280,298" fill="url(#pg3)" role="img" aria-label="Photo of a smiling man with glasses"/>
    <polygon points="470,0 520,0 330,298 280,298" fill="#2f8fe0" opacity=".9"/>
    <polygon points="430,0 466,0 335,195 299,195" fill="#1b1c1f"/>
    <polygon points="426,0 462,0 351,165 315,165" fill="#e8661c"/>
  </svg>
  <div class="brand abs c-brand"><span class="mark"></span>Veltrion Tech</div>
  <div class="abs c-head">Contact Us</div>
  <div class="c-line" style="top:204px"><svg width="9" height="9" viewBox="0 0 10 10"><path d="M2 1l2 0 1 2.5-1.3 1a6 6 0 0 0 2.8 2.8l1-1.3L10 7v2a1 1 0 0 1-1 1A9 9 0 0 1 1 2a1 1 0 0 1 1-1z" fill="#fff"/></svg>(555) 014-2273</div>
  <div class="c-line" style="top:219px"><svg width="9" height="9" viewBox="0 0 10 10"><circle cx="5" cy="5" r="4.2" fill="none" stroke="#fff" stroke-width="1"/><circle cx="5" cy="5" r="1.8" fill="none" stroke="#fff" stroke-width="1"/></svg>info@veltrion.io</div>
  <div class="c-line" style="top:234px"><svg width="9" height="9" viewBox="0 0 10 10"><circle cx="5" cy="5" r="4.2" fill="none" stroke="#fff" stroke-width="1"/><ellipse cx="5" cy="5" rx="1.8" ry="4.2" fill="none" stroke="#fff" stroke-width=".8"/><line x1="1" y1="5" x2="9" y2="5" stroke="#fff" stroke-width=".8"/></svg>www.veltrion.io</div>
  <div class="abs c-bar">Copyright © 2021 Veltrion Technology, LLC. All Rights Reserved.</div>
</article>

</body>
</html>
```